Tarrowie Gymkhana community event

We are looking for a bright new poster for our annual gymkhana event. We are a remote outback town in the Flinders Ranges, South Australia with a very small population (27 people)
Our picnic gymkhana is a community even bringing families amd their ponies from 100 of kms away for a fun filled day.
We have events for junior and senior riders events for spectators and generally lots of fun. Our poster should include our sponsor list, information like live evening entertainment, catering and bar facilities. The event is October 15th 2022.
I have photos etc if you need them will upload them as needed.
Poster should be easy to read and eye catching.

Target Market(s)

Local community

Industry/Entity Type

Horse and family event

Requirements
Must have
• Title sponsor list dates and general information
Nice to have
• Colours

```html
<!DOCTYPE html>
<html lang="en">
<head>
<meta charset="utf-8">
<title>Tarrowie Gymkhana Poster</title>
<link href="https://fonts.googleapis.com/css2?family=Rye&family=Poppins:wght@400;500;600;700;800&family=Bebas+Neue&display=swap" rel="stylesheet">
<style>
  :root {
    --ink: #2b211a;
    --dark-brown: #3b2b1f;
    --mid-brown: #6b4f36;
    --tan: #b0946a;
    --tan-light: #c8ad82;
    --title-fill: #c7a878;
    --paper: #ffffff;
    --grey-band: #e6e6e6;
    --pin: #d42a2a;
  }
  * { box-sizing: border-box; margin: 0; padding: 0; }
  html, body { width: 1200px; height: 1200px; overflow: hidden; background: var(--paper); }
  .poster {
    position: absolute; left: 283px; top: 123px; width: 641px; height: 960px; overflow: hidden;
    background: linear-gradient(180deg, #2f2620 0%, #3b2e24 30%, #6d5640 44%, #a38660 54%, #b1956c 70%, #a68a62 90%);
    font-family: "Poppins", sans-serif; color: var(--ink);
  }
  .abs { position: absolute; }
  .photo { position: absolute; }
  .riders-left { left: 0; top: 175px; width: 236px; height: 222px;
    background: radial-gradient(ellipse at 50% 55%, #8a4a2c 0%, #5a3a28 50%, rgba(59,43,31,0) 75%); }
  .riders-right { left: 345px; top: 175px; width: 296px; height: 322px;
    background: radial-gradient(ellipse at 65% 50%, #8c4c2a 0%, #6a3e26 45%, rgba(90,60,40,0) 75%); }
  .field { left: 0; top: 740px; width: 641px; height: 130px;
    background: linear-gradient(180deg, rgba(160,130,90,0) 0%, rgba(150,120,80,.35) 50%, rgba(160,130,90,0) 100%); }
  .title { left: 0; width: 641px; text-align: center; font-family: "Rye", serif; color: var(--title-fill);
    text-shadow: 2px 0 0 var(--ink), -2px 0 0 var(--ink), 0 2px 0 var(--ink), 0 -2px 0 var(--ink), 3px 4px 0 var(--ink); line-height: 1; }
  .title-main { top: 50px; font-size: 66px; letter-spacing: 1px; }
  .title-sub { top: 128px; font-size: 62px; letter-spacing: 1px; }
  .tagline { left: 160px; width: 330px; top: 208px; text-align: center; color: #fff; font-weight: 600; font-size: 14.5px; line-height: 21px; }
  .date { left: 193px; top: 297px; width: 280px; height: 34px; border: 1.5px solid #e8dcc6; display: flex; align-items: center;
    font-weight: 600; font-size: 24px; }
  .date-day { background: var(--tan-light); color: var(--ink); padding: 0 6px 0 8px; height: 100%; display: flex; align-items: center; }
  .date-year { background: var(--ink); color: var(--tan-light); padding: 0 6px; height: 100%; display: flex; align-items: center; flex: 1; }
  .features { left: 36px; top: 408px; font-family: "Bebas Neue", sans-serif; font-size: 33px; line-height: 31px; }
  .features .light { color: #fff; }
  .features .dark { color: var(--ink); }
  .polaroid { position: absolute; background: #fff; padding: 7px 7px 18px; box-shadow: 0 2px 5px rgba(0,0,0,.35); }
  .polaroid .pic { width: 100%; height: 100%; }
  .polaroid .pin { position: absolute; top: -6px; left: 50%; width: 10px; height: 10px; border-radius: 50%; background: var(--pin); }
  .p1 { left: -8px; top: 520px; width: 118px; height: 140px; transform: rotate(5deg); }
  .p2 { left: 110px; top: 518px; width: 128px; height: 145px; transform: rotate(-9deg); }
  .p3 { left: 388px; top: 478px; width: 145px; height: 162px; transform: rotate(6deg); }
  .p4 { left: 530px; top: 472px; width: 125px; height: 145px; transform: rotate(-8deg); }
  .p1 .pic { background: linear-gradient(180deg, #8fb7de 0%, #a7b9c4 35%, #9c7b5a 70%, #c7a27a 100%); }
  .p2 .pic { background: linear-gradient(180deg, #9aa4b8 0%, #b07a5c 50%, #3d3a5a 100%); }
  .p3 .pic { background: linear-gradient(180deg, #8ab3e0 0%, #9fb3c6 30%, #6f6f7e 65%, #e2ddd6 100%); }
  .p4 .pic { background: linear-gradient(180deg, #6b5031 0%, #d1a24a 45%, #4a3826 100%); }
  .badge { left: 242px; top: 516px; width: 144px; height: 144px; }
  .badge-text { position: absolute; left: 242px; top: 530px; width: 144px; text-align: center; color: #fff; }
  .badge-price { font-family: "Bebas Neue", sans-serif; font-size: 74px; line-height: 66px; }
  .badge-price sup { font-size: 32px; vertical-align: 28px; }
  .badge-label { color: var(--tan-light); font-weight: 700; font-size: 16px; line-height: 16px; }
  .badge-note { font-size: 7px; font-weight: 500; }
  .label { background: var(--dark-brown); color: #fff; font-weight: 700; font-size: 20px; padding: 3px 9px; border-radius: 3px; }
  .horse-label { left: 37px; top: 694px; width: 180px; height: 36px; }
  .horse-frame { left: 37px; top: 712px; width: 180px; height: 88px; border: 2px solid #efe6d6; border-left: none; border-radius: 0 4px 4px 0; width: 198px; left: 37px; }
  .horse-frame-bar { left: 37px; top: 797px; width: 35px; height: 5px; background: #ddd; border-radius: 2px; }
  .horse-info { left: 37px; top: 738px; font-size: 10.5px; line-height: 15.5px; color: var(--ink); }
  .horse-info .head { font-weight: 600; font-size: 10.5px; }
  .horse-info b { font-weight: 700; }
  .cause { left: 37px; top: 811px; color: var(--ink); font-weight: 700; font-size: 16px; line-height: 18px; }
  .no-byo { left: 37px; top: 829px; color: #fff; font-weight: 800; font-size: 24px; line-height: 28px; }
  .nonhorse-label { left: 359px; top: 683px; width: 244px; height: 36px; background: #fff; color: var(--ink); border-radius: 3px;
    font-weight: 700; font-size: 20px; text-align: center; line-height: 36px; }
  .nominations { left: 360px; top: 722px; display: flex; align-items: center; gap: 8px; }
  .nominations .price { font-weight: 800; font-size: 32px; color: #fff; line-height: 30px; }
  .nominations .price sup { font-size: 17px; vertical-align: 12px; }
  .nominations .desc { font-weight: 700; font-size: 14px; line-height: 15.5px; color: var(--ink); }
  .nominations .desc .muted { color: #6e5a43; }
  .contact-head { left: 356px; top: 764px; width: 250px; font-weight: 700; font-size: 17px; color: var(--ink); border-bottom: 1px solid #efe6d6; padding-bottom: 1px; }
  .contact { left: 358px; top: 788px; width: 248px; font-size: 10px; line-height: 12px; font-weight: 600; color: #fff; border-bottom: 1px solid #efe6d6; padding-bottom: 3px; }
  .contact span { color: #5a4632; }
  .notes { left: 358px; top: 818px; font-size: 11px; line-height: 14px; color: var(--ink); }
  .torn { left: 0; top: 870px; width: 641px; height: 90px; }
  .sponsors { left: 0; top: 912px; width: 641px; text-align: center; font-size: 10.5px; font-weight: 500; color: var(--ink); }
</style>
</head>
<body>
<div class="poster">
  <div class="photo riders-left" role="img" aria-label="Photo of two riders on horses competing in a gymkhana race"></div>
  <div class="photo riders-right" role="img" aria-label="Photo of junior riders on chestnut horses"></div>
  <div class="photo abs field" role="img" aria-label="Faint photo of riders racing across a dusty field"></div>

  <h1 class="abs title title-main">TARROWIE</h1>
  <div class="abs title title-sub">GYMKHANA</div>

  <p class="abs tagline">COME AND JOIN US AT ONE OF SOUTH AUSTRALIA'S LONGEST RUNNING GYMKHANAS</p>

  <div class="abs date"><span class="date-day">OCTOBER 15TH</span><span class="date-year">2022</span></div>

  <div class="abs features">
    <div class="light">FOOD &amp; BAR FACILITIES ALL DAY</div>
    <div class="dark">EVENING ENTERTAINMENT</div>
    <div class="light">ROAST DINNER</div>
  </div>

  <div class="polaroid p1"><div class="pic" role="img" aria-label="Photo of a wool bale rolling race"></div><span class="pin"></span></div>
  <div class="polaroid p2"><div class="pic" role="img" aria-label="Photo of a child holding a trophy on a pony"></div><span class="pin"></span></div>
  <div class="polaroid p3"><div class="pic" role="img" aria-label="Photo of spectators chatting in the sun"></div><span class="pin"></span></div>
  <div class="polaroid p4"><div class="pic" role="img" aria-label="Photo of evening dancing in the hall"></div><span class="pin"></span></div>

  <svg class="abs badge" viewBox="0 0 144 144" aria-hidden="true">
    <polygon fill="#3b2b1f" stroke="#f3ead9" stroke-width="2"
      points="72,2 80,12 91,5 96,17 108,13 110,25 123,25 121,37 133,40 127,51 138,57 129,66 138,72 129,78 138,87 127,93 133,104 121,107 123,119 110,119 108,131 96,127 91,139 80,132 72,142 64,132 53,139 48,127 36,131 34,119 21,119 23,107 11,104 17,93 6,87 15,78 6,72 15,66 6,57 17,51 11,40 23,37 21,25 34,25 36,13 48,17 53,5 64,12"/>
  </svg>
  <div class="badge-text">
    <div class="badge-price"><sup>$</sup>15</div>
    <div class="badge-label">ADMISSION</div>
    <div class="badge-note">*CHILDREN U/15 FREE</div>
  </div>

  <div class="abs horse-frame"></div>
  <div class="abs horse-frame-bar"></div>
  <div class="abs label horse-label">HORSE EVENTS</div>
  <div class="abs horse-info">
    <div class="head">&nbsp;GYMKHANA EVENT NOMINATIONS-</div>
    <div>Junior - <b>$20.00</b> &nbsp;Senior - <b>$30.00</b></div>
    <div>For the day(per horse).</div>
  </div>
  <div class="abs cause">HELP SUPPORT THE CAUSE</div>
  <div class="abs no-byo">NO BYO ALCOHOL</div>

  <div class="abs nonhorse-label">NON-HORSE EVENTS</div>
  <div class="abs nominations">
    <div class="price"><sup>$</sup>2</div>
    <div class="desc">ALL NOMINATIONS<br><span class="muted">PER PERSON PER EVENT</span></div>
  </div>
  <div class="abs contact-head">FOR MORE INFO CONTACT</div>
  <div class="abs contact">
    <div><span>KATE DUNSTAN -</span> 8600 1234</div>
    <div><span>EMAIL -</span> tarrowiegymkhana@mail.com</div>
  </div>
  <div class="abs notes">*All riders ride at their own risk.<br>&nbsp;Dogs must be on leash at all times.</div>

  <svg class="abs torn" viewBox="0 0 641 90" preserveAspectRatio="none" aria-hidden="true">
    <path fill="#e4e4e4" d="M0,8 L20,4 L38,10 L60,5 L85,12 L110,6 L140,11 L170,4 L200,12 L230,7 L262,13 L290,6 L320,11 L350,5 L380,12 L410,7 L440,13 L470,6 L500,10 L530,4 L560,11 L590,6 L620,12 L641,7 L641,90 L0,90 Z"/>
    <path fill="none" stroke="#5a3e28" stroke-width="3" d="M0,8 L20,4 L38,10 L60,5 L85,12 L110,6 L140,11 L170,4 L200,12 L230,7 L262,13 L290,6 L320,11 L350,5 L380,12 L410,7 L440,13 L470,6 L500,10 L530,4 L560,11 L590,6 L620,12 L641,7"/>
  </svg>
  <div class="abs sponsors">*THANKS TO ALL OUR GENEROUS SPONSORS*</div>
</div>
</body>
</html>
```